WP website design (Brisden)

We need a wordpress design for an established auction and real estate company based in Kentucky. The winning design will incorporate a professional color scheme with company logo in a clean layout with specified widgets. The design needs to consider that this will be developed on a responsive theme. Color is #307d84, with gray/black or other as an accent/highlight color.

Industry/Entity Type

Real Estate

Requirements
Must have
• Elelments of design need to consider that this site is going to be developed on a responsive theme.

Navigation:
1) Home 2) Current Auctions 3) Past Auctions 4) Meet the Staff 5) For Sellers 6) For Buyers 7) Testimonials 8) Contact Us

Colors will be the blue of logo plus black/gray or other accent color.

Slideshow will be prominent, please use stock real estate photo for initial image. Will have following in either header or sidebar: testimonials, social icons (FB, linkedin Twitter, RSS), Featured Auctions widget, newsletter signup form.

Footer will have contact info (below) and attached affiliation logos.
Brisden Auctions, Inc.
48710 Pomeroy Rd., Louisville KY 40199
dan.office@brisdenbid.example
Phone: (502) 555 0172

```html
<!DOCTYPE html>
<html lang="en">
<head>
<meta charset="utf-8">
<title>Brisden Auctions, Inc.</title>
<link href="https://fonts.googleapis.com/css2?family=Arimo:wght@400;700&family=Didact+Gothic&family=Roboto+Condensed:ital,wght@0,400;1,400&family=Roboto:ital@1&display=swap" rel="stylesheet">
<style>
:root{
  --teal:#307d84;
  --teal-dark:#22636a;
  --teal-deep:#1d5a60;
  --ink:#111;
  --text:#333;
  --page:#f1f1f1;
  --card:#fff;
  --line:#dcdcdc;
  --red:#d8262b;
  --orange:#e8531d;
  --gold:#f7b733;
}
*{margin:0;padding:0;box-sizing:border-box}
html,body{width:957px;height:1200px;overflow:hidden}
body{position:relative;background:var(--page);font-family:"Didact Gothic",sans-serif;color:var(--text)}
.abs{position:absolute}
.topline{left:0;top:0;width:957px;height:6px;background:var(--teal)}
.header{left:0;top:6px;width:957px;height:377px;background:linear-gradient(180deg,#f5f5f5 0%,#dedede 100%)}
.brand{left:123px;top:26px;display:flex;align-items:center;gap:10px}
.brand-mark{width:36px;height:36px;background:var(--teal)}
.brand-name{font-family:"Arimo",sans-serif;font-weight:700;font-size:30px;color:var(--teal);line-height:1}
.brand-sub{left:169px;top:64px;font-family:"Arimo",sans-serif;font-weight:700;font-size:16px;color:var(--teal)}
.social{left:703px;top:20px;display:flex;gap:9px}
.social span{width:26px;height:26px;border-radius:50%;background:#8a8a8a;box-shadow:inset 0 0 0 2px #a9a9a9}
.phone{left:684px;top:76px;display:flex;align-items:center;gap:6px;font-family:"Arimo",sans-serif;font-size:21px;color:var(--teal)}
.nav{left:109px;top:107px;width:740px;height:31px;background:var(--ink);display:flex;justify-content:space-around;align-items:center;padding:0 4px}
.nav a{color:#fff;text-decoration:none;font-family:"Arimo",sans-serif;font-size:11.5px}
.slider{left:109px;top:138px;width:740px;height:245px;background:linear-gradient(180deg,#bcd6a3 0%,#8aa383 35%,#6f8a5c 70%,#4e8a2e 100%)}
.slide-arrow{top:245px;width:30px;height:30px;border-radius:50%;background:rgba(0,0,0,.5)}
.dots{left:447px;top:365px;display:flex;gap:3px}
.dots span{width:12px;height:12px;background:#fff;border:1px solid #ccc}
.dots span.on{background:#9a2a2a}
.main{left:109px;top:383px;width:740px;height:696px;background:#f7f7f7}
h1.welcome{left:123px;top:401px;font-family:"Arimo",sans-serif;font-weight:400;font-size:22px;color:var(--ink)}
.intro{left:123px;top:429px;width:490px;font-size:11.2px;line-height:15px}
h2.section{left:122px;top:513px;font-family:"Arimo",sans-serif;font-weight:400;font-size:19px;color:var(--ink)}
.pager{left:572px;top:514px;display:flex;gap:10px}
.card{left:123px;width:493px;height:256px;background:#f2f2f2;border:1px solid var(--line)}
.thumb{left:10px;top:9px;width:139px;height:107px;background:#fff;border:1px solid #ccc;padding:5px}
.thumb div{width:100%;height:100%;background:linear-gradient(180deg,#c7d6e4 0%,#b8a89a 55%,#6e7d55 100%)}
.details{left:10px;top:122px;width:139px;height:30px;background:var(--teal);border-bottom:3px solid var(--teal-deep);border-radius:2px;color:#fff;font-size:17px;display:flex;align-items:center;justify-content:center;gap:8px}
.info{left:160px;top:9px;width:318px;height:86px;background:var(--card);border:1px solid var(--line);padding:10px 12px}
.info h3{font-family:"Roboto Condensed",sans-serif;font-weight:400;font-size:14.5px;color:var(--teal)}
.info em{display:block;font-family:"Roboto",sans-serif;font-size:9.5px;color:var(--orange);margin:5px 0 4px}
.info p{font-size:11.5px;line-height:15px;color:#222}
.desc{left:160px;top:104px;width:318px;height:122px;background:var(--card);border:1px solid var(--line);padding:12px 12px;font-size:10.2px;line-height:15.2px;color:#222}
.watch{left:175px;top:216px;width:292px;height:27px;background:var(--teal);border-bottom:3px solid var(--teal-deep);color:#fff;font-family:"Roboto",sans-serif;font-style:italic;font-size:13px;display:flex;align-items:center;justify-content:center}
.side-box{left:632px;width:202px;background:var(--teal)}
.subscribe{top:385px;height:142px}
.ribbon{left:625px;top:388px;width:187px;height:28px;background:var(--red);color:#fff;font-family:"Arimo",sans-serif;font-weight:700;font-size:18px;padding:2px 0 0 23px}
.sub-text{left:640px;top:423px;width:186px;text-align:center;color:#fff;font-family:"Roboto",sans-serif;font-style:italic;font-size:12.5px;line-height:15px}
.email{left:646px;top:478px;width:140px;height:32px;border:1px solid #8fc0c4;color:#cfe5e6;font-size:10px;padding:10px 6px}
.go{left:786px;top:478px;width:33px;height:32px;background:var(--gold);color:#222;font-family:"Arimo",sans-serif;font-weight:700;font-size:14px;display:flex;align-items:center;justify-content:center}
.featured{top:543px;height:232px}
.side-title{left:646px;width:173px;height:24px;background:var(--ink);color:#fff;font-family:"Arimo",sans-serif;font-size:15px;text-align:center;line-height:24px}
.feat-img{left:646px;top:575px;width:173px;height:95px;background:linear-gradient(180deg,#b9cfe6 0%,#a49584 55%,#5d7a47 100%)}
.feat-text{left:646px;top:675px;width:176px;color:#fff;font-size:11.8px;line-height:12.5px}
.btn-small{height:26px;border-radius:3px;font-family:"Arimo",sans-serif;font-size:9.5px;display:flex;align-items:center;justify-content:center;gap:6px}
.learn{left:688px;top:742px;width:88px;background:var(--gold);color:#333;border-bottom:2px solid #c88a18}
.testi{left:632px;top:790px;width:202px;height:274px;background:#fff}
.testi-title{left:646px;top:798px;width:173px;height:25px;background:var(--teal-dark);border:1px solid #111;color:#fff;font-family:"Arimo",sans-serif;font-size:15px;text-align:center;line-height:23px}
.quote{left:646px;top:830px;width:172px;font-family:"Roboto",sans-serif;font-style:italic;font-size:11.6px;line-height:16.6px;color:#333}
.author{left:700px;top:977px;width:116px;text-align:right;font-family:"Roboto",sans-serif;font-style:italic;font-weight:700;font-size:13px;line-height:17px;color:var(--teal)}
.viewall{left:689px;top:1023px;width:88px;background:var(--teal-dark);color:#fff;border-bottom:2px solid #0f3c40}
.footer{left:0;top:1079px;width:957px;height:94px;background:var(--teal)}
.f-addr{left:123px;top:1101px;color:#fff;font-size:12px;line-height:16px}
.f-contact{left:281px;top:1101px;color:#fff;font-size:12px;line-height:16px}
.f-contact div{display:flex;align-items:center;gap:6px}
.badges{left:530px;top:1106px;display:flex;align-items:center;gap:10px}
.badges span{background:#1b1b1b}
.copy{left:0;top:1173px;width:957px;height:27px;background:var(--teal-deep);color:#cfe3e5;font-size:9.5px;text-align:center;line-height:27px;letter-spacing:.4px}
</style>
</head>
<body>
<div class="abs topline"></div>
<header class="abs header"></header>
<div class="abs brand"><span class="brand-mark"></span><span class="brand-name">BRISDEN</span></div>
<div class="abs brand-sub">AUCTIONS inc.</div>
<div class="abs social" aria-label="Social links"><span></span><span></span><span></span><span></span></div>
<div class="abs phone">
  <svg width="22" height="22" viewBox="0 0 24 24"><path d="M6.6 10.8a15 15 0 0 0 6.6 6.6l2.2-2.2c.3-.3.7-.4 1-.2 1.1.4 2.3.6 3.6.6.6 0 1 .4 1 1V20c0 .6-.4 1-1 1A17 17 0 0 1 3 4c0-.6.4-1 1-1h3.5c.6 0 1 .4 1 1 0 1.3.2 2.5.6 3.6.1.3 0 .7-.2 1z" fill="#222"/><path d="M15 3a6 6 0 0 1 6 6M15 6a3 3 0 0 1 3 3" stroke="#f39c12" stroke-width="2" fill="none"/></svg>
  (502) 555 0172
</div>
<nav class="abs nav">
  <a>Home</a><a>Current Auctions</a><a>Past Auctions</a><a>Meet the Staff</a><a>For Sellers</a><a>For Buyers</a><a>Testimonials</a><a>Contact Us</a>
</nav>
<div class="abs slider" role="img" aria-label="Two-storey family home with front porch, garden and lawn under trees"></div>
<div class="abs slide-arrow" style="left:121px"><svg width="30" height="30"><path d="M18 8l-7 7 7 7" stroke="#fff" stroke-width="2" fill="none"/></svg></div>
<div class="abs slide-arrow" style="left:806px"><svg width="30" height="30"><path d="M12 8l7 7-7 7" stroke="#fff" stroke-width="2" fill="none"/></svg></div>
<div class="abs dots"><span class="on"></span><span></span><span></span><span></span></div>

<main class="abs main"></main>
<h1 class="abs welcome">Welcome to Brisden Auctions Inc.</h1>
<p class="abs intro">Lorem Ipsum proin gravida nibh vel velit auctor aliquet. Aenean sollicitudin, lorem quis bibendum auctor, nisi elit consequat ipsum, nec sagittis sem nibh id elit. Duis sed odio sit amet nibh vulputate cursus a sit amet mauris. Morbi accumsan ipsum velit..</p>
<h2 class="abs section">Current Auctions</h2>
<div class="abs pager">
  <svg width="16" height="14"><path d="M15 7H2M7 2L2 7l5 5" stroke="#333" stroke-width="1.6" fill="none"/></svg>
  <svg width="16" height="14"><path d="M1 7h13M9 2l5 5-5 5" stroke="#333" stroke-width="1.6" fill="none"/></svg>
</div>

<article class="abs card" style="top:540px">
  <div class="abs thumb"><div role="img" aria-label="Brick and timber two-storey house"></div></div>
  <div class="abs details"><svg width="18" height="18"><circle cx="7" cy="7" r="5" fill="#dfe9ea" stroke="#fff" stroke-width="2"/><path d="M11 11l5 5" stroke="#fff" stroke-width="3"/></svg>Details</div>
  <div class="abs info"><h3>BUSINESS LIQUIDATION - PERSONAL PROPERTY</h3><em>Personal Property Online Auction coming in July/Aug.</em><p>Located at Harlan Organ Works, 4120 Ridgeway Industrial Blvd., Louisville, KY 40288</p></div>
  <div class="abs desc">Personal Property Online Auction: Remaining assets of Harlan Organ Works – 2006 Stridon van; 2007 Halvern Grand Tourer; 2006 Korvel Sedan; 2002 Ardent Cruiser; Bramwell 4,000 lb. forklift; Halsted 80 gal. air compressor; MR 18 band saw; 12" Tolliver jointer; drill press; ladders; tools; fittings; office furniture &amp; equipment; unusual &amp; unique items.</div>
  <div class="abs watch">Please watch for upcoming online bidding.</div>
</article>

<article class="abs card" style="top:809px">
  <div class="abs thumb"><div role="img" aria-label="Brick and timber two-storey house"></div></div>
  <div class="abs details"><svg width="18" height="18"><circle cx="7" cy="7" r="5" fill="#dfe9ea" stroke="#fff" stroke-width="2"/><path d="M11 11l5 5" stroke="#fff" stroke-width="3"/></svg>Details</div>
  <div class="abs info"><h3>BUSINESS LIQUIDATION - PERSONAL PROPERTY</h3><em>Personal Property Online Auction coming in July/Aug.</em><p>Located at Harlan Organ Works, 4120 Ridgeway Industrial Blvd., Louisville, KY 40288</p></div>
  <div class="abs desc">Personal Property Online Auction: Remaining assets of Harlan Organ Works – 2006 Stridon van; 2007 Halvern Grand Tourer; 2006 Korvel Sedan; 2002 Ardent Cruiser; Bramwell 4,000 lb. forklift; Halsted 80 gal. air compressor; MR 18 band saw; 12" Tolliver jointer; drill press; ladders; tools; fittings; office furniture &amp; equipment; unusual &amp; unique items.</div>
  <div class="abs watch">Please watch for upcoming online bidding.</div>
</article>

<aside>
  <div class="abs side-box subscribe"></div>
  <div class="abs ribbon">Subscribe Now</div>
  <p class="abs sub-text">To stay updated with all upcomig Auction, please enter your email address bellow</p>
  <div class="abs email">Enter email ID</div>
  <div class="abs go">GO</div>

  <div class="abs side-box featured"></div>
  <div class="abs side-title" style="top:550px">Featured Auctions</div>
  <div class="abs feat-img" role="img" aria-label="Three-storey townhouse with garages"></div>
  <p class="abs feat-text">Lorem Ipsum. Pro gravida nibh vel velit auctor aliqu et. Aenean so llic itudin, lorem quis bibe nd um auctor, nisi elit consequa uat ipsum..</p>
  <div class="abs btn-small learn">Learn more <svg width="16" height="8"><path d="M0 4h14M11 1l3 3-3 3" stroke="#e8a010" stroke-width="1.5" fill="none"/></svg></div>

  <div class="abs testi"></div>
  <div class="abs testi-title">Testimonials</div>
  <p class="abs quote">Lorem Ipsum. Proin gravida nibh vel velit auctor aliquet. Aenean sollicitudin, lorem quis biben du m auctor, nisi elit consequat ipsum, nec sagittis sem nibh id elit. Duis sed odio sit amet nibh vulputate cursus a sit amet ma uris..</p>
  <div class="abs author">- Darren,<br>Kentucky</div>
  <div class="abs btn-small viewall">View all <svg width="16" height="8"><path d="M0 4h14M11 1l3 3-3 3" stroke="#f7d23a" stroke-width="1.5" fill="none"/></svg></div>
</aside>

<footer class="abs footer"></footer>
<div class="abs f-addr">Brisden Auctions, Inc.<br>48710 Pomeroy Rd.,<br>Louisville KY 40199</div>
<div class="abs f-contact">
  <div><svg width="11" height="11"><rect x="1" y="3" width="9" height="7" fill="#f7b733"/><path d="M1 3l4.5-2 4.5 2" stroke="#f7b733" fill="none"/></svg>dan.office@brisdenbid.example</div>
  <div><svg width="11" height="11"><path d="M2 6a6 6 0 0 0 3 3l1-1 2 1v2A9 9 0 0 1 0 3V1h2l1 2-1 1z" fill="#f7b733"/></svg>(502) 555 0172</div>
</div>
<div class="abs badges" aria-label="Affiliations">
  <span style="width:100px;height:44px;border-radius:50%;background:#2a4f8a"></span>
  <span style="width:40px;height:44px"></span>
  <span style="width:30px;height:46px"></span>
  <span style="width:44px;height:42px"></span>
  <span style="width:40px;height:44px"></span>
</div>
<div class="abs copy">Copyright © 2014 Brisden Auctions Ins | All Rights Reserved.</div>
</body>
</html>
```